Pellano Growth Brochure Design Project

- Who we are?
Pellano Growth is New Internet Marketing Company Based in China.

It is our aim to provide Chinese clients with the means to internationally market their product, via the Internet.

Our primary products are Outsourced Design ( Thanks to Artwell hub and the amazing designers who use it), SEO and Virtual Hosting.

- Project Brief
Design a vibrant and fresh brochure that introduces the fundamentals of SEO. There is no restriction to the number of pages, however all the info I have included in this brief must be included.

- Colour Palette
Please see link or download the Vantoria Swatch Exchange File or follow the link below
http://hues.vantoria-sample.com/#themes/search?term=4817350

Logo updated - grey background removed

Various file formats added for logo and brochure content

Brochure zip file add containing logo in different formats.

Vantoria color scheme file added

The general corporate colors are:

Base Color: CMYK :0, 60, 80, 0  Hex: FF6633
Dark Orange: CMYK: 0, 72, 96, 30 Hex: B23308
Light Orange: CMYK 0, 42, 56, 0 Hex: FF9571
Grey: CMYK 0, 0, 0, 48 Hex: 858585
Light Grey: CMYK 0, 0, 0, 26 Hex: BDBDBD

Please note that I'm happy for other colors to be included, however I would like these the corporate branding colors to be clearly present through the brochure.

Hi All

First place payment has increased to $600 - Looking to see some creative designs!

Hi All

Reason: I have increase the budget and extend the deadline as I need to see more design.

I have attached a zip file that contains example brochures I like.

We are not keen on the table data its a little plain. We have create an info-graphic to replace one of the table and would like to see it included in the design.

Reason: A few designers have asked for this extension and I would like to see additional designs. Thanks Marek

Target Market(s)

- Our Target Audience is..
It is small to medium businesses looking to reach out to the international market.
Our clients still very much operate on a face to face level in business and are new to the concept of Internet marketing

However this must look professional, Marketable and Clean, with the power of connecting people globally, through SEO and design to be reflected visually in the brochure.

Industry/Entity Type

Internet

Requirements
Must have
• One or more of the FACTS that I have highlighted need to stand out on each page. These FACTS can be found the document attached to this brief and are under the section titled 'Did You Know!'. Not every fact in this section needs to be highlighted in the brochure, but each page needs to have at least, one or more fact that stands out, soemwhere on the page.
See attached document, under the heading 'Did you Know!' and use one or two of these facts to spruce up the pages!

One image/ per page or per two pages MUST be included!

- Provide stock photos and please send us a message with the additional cost of these with your submission

The Table data, that I have included in the attachment must be included in the body of the pages - BUT the table format is not necessary and you can place the information in the body like plain text.

The brochure size should be a little larger than A4.

Please design the back page, like a pocket to hold paper and other material in it that I include with this brochure.

```html
<!DOCTYPE html>
<html lang="en">
<head>
<meta charset="utf-8">
<title>Pellano Growth – Pocket Folder</title>
<link rel="stylesheet" href="https://fonts.googleapis.com/css2?family=Open+Sans:wght@400;600;700&family=Roboto+Condensed:wght@700&display=swap">
<style>
  :root {
    --stage-top: #0a6cb8;
    --stage-bottom: #020748;
    --paper-grey: #d1d2d4;
    --brand-orange: #f15a24;
    --dark-orange: #b23308;
    --mid-grey: #858585;
    --light-grey: #bdbdbd;
    --faint-grey: #c6c7c9;
    --white: #ffffff;
    --ink: #1a1a1a;
  }
  * { margin: 0; padding: 0; box-sizing: border-box; }
  html, body { width: 1200px; height: 900px; overflow: hidden; }
  body {
    position: relative;
    background: linear-gradient(180deg, var(--stage-top) 0%, #063a88 45%, var(--stage-bottom) 100%);
    font-family: "Open Sans", Arial, sans-serif;
  }
  .spread { position: absolute; left: 67px; top: 79px; width: 1066px; height: 743px; background: var(--paper-grey); overflow: hidden; }

  /* brand lockups */
  .brand { position: absolute; display: flex; align-items: center; }
  .brand-dot { border-radius: 50%; border: 4px solid var(--brand-orange); flex: none; }
  .brand-text { margin-left: 8px; line-height: 1; }
  .brand-name { font-weight: 700; color: var(--brand-orange); letter-spacing: -0.3px; }
  .brand-tag { display: block; font-weight: 600; color: var(--ink); margin-top: 3px; }

  /* back page: pocket */
  .back-brand { left: 138px; top: 44px; }
  .back-brand .brand-dot { width: 44px; height: 44px; }
  .back-brand .brand-name { font-size: 16px; }
  .back-brand .brand-tag { font-size: 7px; }

  .insert-sheet { position: absolute; left: 57px; top: 103px; width: 362px; height: 520px; background: var(--white); border-radius: 28px 28px 0 0; }
  .insert-title { margin-top: 12px; text-align: center; font-size: 14px; font-weight: 700; color: var(--ink); letter-spacing: 0.2px; }
  .insert-mark { position: absolute; left: 66px; top: 247px; }
  .insert-mark .brand-dot { width: 58px; height: 58px; border-color: var(--faint-grey); }
  .insert-mark .brand-name { font-size: 20px; color: var(--faint-grey); }
  .insert-mark .brand-tag { font-size: 8px; color: var(--faint-grey); font-weight: 400; }

  .pocket { position: absolute; left: 33px; top: 518px; width: 412px; height: 180px; }
  .pocket-address { position: absolute; left: 33px; top: 598px; width: 412px; text-align: center; color: var(--white); font-size: 11px; line-height: 14px; }
  .pocket-address .small { font-size: 9.5px; line-height: 12px; }

  /* spine */
  .spine { position: absolute; left: 476px; top: 0; width: 82px; height: 743px; background: var(--brand-orange); }
  .spine-fold { position: absolute; left: 533px; top: 0; width: 1px; height: 743px; background: #d94e1c; }

  /* front page */
  .front-brand { left: 767px; top: 230px; }
  .front-brand .brand-dot { width: 66px; height: 66px; border-width: 5px; }
  .front-brand .brand-name { font-size: 24px; }
  .front-brand .brand-tag { font-size: 9px; font-weight: 400; }

  .photo-strip { position: absolute; left: 558px; top: 335px; width: 80px; height: 72px; }
  .photo-tile { position: absolute; top: 335px; width: 78px; height: 72px; border: 1px dashed var(--brand-orange); border-radius: 8px 14px 8px 14px; }
  .tile-1 { left: 660px; background: linear-gradient(135deg, #7a5a4c, #e7e7e7 55%, #a9a9a9); }
  .tile-2 { left: 761px; background: linear-gradient(135deg, #f2f2f2, #cfcfcf 60%, #a77e66); }
  .tile-3 { left: 863px; background: linear-gradient(135deg, #efefef, #b7b7b7 50%, #dcdcdc); }
  .tile-4 { left: 963px; background: linear-gradient(135deg, #9a9a9a, #e0e0e0 50%, #7b7b7b); }

  .service-list { position: absolute; left: 558px; top: 439px; list-style: none; }
  .service { position: relative; height: 19px; margin-bottom: 16.6px; padding-left: 26px; background: var(--brand-orange);
             clip-path: polygon(0 0, calc(100% - 10px) 0, 100% 50%, calc(100% - 10px) 100%, 0 100%, 0 0);
             font-family: "Roboto Condensed", "Arial Narrow", sans-serif; font-weight: 700; font-size: 12.5px; line-height: 19px; color: var(--white); }

  .word-band { position: absolute; left: 558px; top: 671px; width: 392px; height: 72px;
               background: linear-gradient(90deg, #c9c9c9 0%, #e58a63 25%, var(--brand-orange) 60%, #e9703e 100%); }
  .globe-hands { position: absolute; left: 918px; top: 640px; width: 148px; height: 103px; border-radius: 60px 0 0 0;
                 background: linear-gradient(160deg, #e8e8e8, #9ea3a8 60%, #6e7378); }
</style>
</head>
<body>
  <main class="spread">
    <!-- back page -->
    <div class="brand back-brand">
      <span class="brand-dot"></span>
      <span class="brand-text"><span class="brand-name">PellanoGrowth.com</span><span class="brand-tag">SEO and Cloud Consultant</span></span>
    </div>

    <section class="insert-sheet">
      <h2 class="insert-title">Price Lists and Other Promotional Material</h2>
      <div class="brand insert-mark">
        <span class="brand-dot"></span>
        <span class="brand-text"><span class="brand-name">PellanoGrowth.com</span><span class="brand-tag">SEO and Cloud Consultant</span></span>
      </div>
    </section>

    <svg class="pocket" viewBox="0 0 412 180" aria-hidden="true">
      <defs>
        <linearGradient id="pocketFill" x1="0" y1="0" x2="1" y2="0">
          <stop offset="0" stop-color="#8e8e8e"/>
          <stop offset="0.35" stop-color="#cf6c4c"/>
          <stop offset="0.5" stop-color="#e2552a"/>
          <stop offset="0.65" stop-color="#cf6c4c"/>
          <stop offset="1" stop-color="#8e8e8e"/>
        </linearGradient>
      </defs>
      <path d="M4 12 Q206 110 408 12 L408 166 L4 166 Z" fill="url(#pocketFill)"/>
      <path d="M4 166 L408 166" stroke="#b9b9b9" stroke-width="3"/>
      <rect x="0" y="2" width="4" height="170" fill="#ffffff"/>
      <rect x="408" y="2" width="4" height="170" fill="#ffffff"/>
    </svg>
    <address class="pocket-address">
      -: Addres :-<br>
      Lorem ipsum dolor sit amet,<br>
      consectetur adipiscing elit,<br>
      Maecenas luctus pulvinar sapien.<br>
      <span class="small">Website : luctus_pulvinar.com<br>Tele : 1111111111</span>
    </address>

    <!-- spine -->
    <div class="spine"></div>
    <div class="spine-fold"></div>

    <!-- front page -->
    <div class="brand front-brand">
      <span class="brand-dot"></span>
      <span class="brand-text"><span class="brand-name">PellanoGrowth.com</span><span class="brand-tag">SEO and Cloud Consultant</span></span>
    </div>

    <svg class="photo-strip" viewBox="0 0 80 72" aria-hidden="true">
      <path d="M0 0 H76 Q62 36 76 72 H0 Z" fill="var(--brand-orange)"/>
    </svg>
    <div class="photo-tile tile-1" role="img" aria-label="Photo of a hand fitting an SEO puzzle piece"></div>
    <div class="photo-tile tile-2" role="img" aria-label="Photo of a hand sketching a light bulb idea"></div>
    <div class="photo-tile tile-3" role="img" aria-label="Photo of wooden blocks spelling social media"></div>
    <div class="photo-tile tile-4" role="img" aria-label="Photo of a head silhouette filled with internet words"></div>

    <ul class="service-list">
      <li class="service" style="width:78px">SEO</li>
      <li class="service" style="width:95px">Blog</li>
      <li class="service" style="width:113px">Logo Design</li>
      <li class="service" style="width:130px">SEO Packages</li>
      <li class="service" style="width:148px">Website Design</li>
      <li class="service" style="width:290px">Cloud computing and International Hosting</li>
    </ul>

    <div class="word-band" role="img" aria-label="Word collage of social media, vision and growth themes"></div>
    <div class="globe-hands" role="img" aria-label="Photo of hands holding a globe"></div>
  </main>
</body>
</html>
```